Label for packages of Pure Raw Natural Honeycomb

This is a label that will be used to sell pure raw honeycomb on the internet and in farm gate sales
Label must contain my Logo (which is attached)
my website www.hivelanterngold.ca
the weight 300 gr and the words Pure Raw Honeycomb
label design should fit onto a sticker 3" by 2" oval but If the size appears to small to get all that info on I am willing to look at a different size or shape

Target Market(s)

internet and in person farm gate customers

Industry/Entity Type

Agriculture

Font styles to use
Other font styles liked:
• the font should compliment my logo font

Colors
ffc214

Requirements
Must have
• Label must contain my Logo (attached) my website www.hivelanterngold.ca
• the weight 300 gr and the words Pure Raw Honeycomb would like something in black and gold with a bit of an Elegant vintage feel
Nice to have
• vintage feel
• If the size appears to small to get all that info on I am willing to look at a different size or shape
Should not have
• no cartoons

```html
<!DOCTYPE html>
<html lang="en">
<head>
<meta charset="utf-8">
<title>Pure Raw Honeycomb Label</title>
<link rel="stylesheet" href="https://fonts.googleapis.com/css2?family=Great+Vibes&family=Open+Sans:wght@600;700&display=swap">
<style>
  :root {
    --backdrop: #ececea;
    --label-black: #0c0c0c;
    --honey-gold: #ffc214;
    --rim-gold: #e9a81a;
    --text-white: #ffffff;
  }
  html, body {
    margin: 0;
    padding: 0;
    width: 1200px;
    height: 1101px;
    overflow: hidden;
    background: var(--backdrop);
  }
  .label-canvas {
    display: block;
    width: 1200px;
    height: 1101px;
  }
  .label-body { fill: var(--label-black); }
  .label-rim { fill: none; stroke: var(--rim-gold); stroke-width: 4; }
  .product-title {
    font-family: "Great Vibes", cursive;
    font-size: 58px;
    fill: var(--honey-gold);
    letter-spacing: 1px;
  }
  .brand-name {
    font-family: "Great Vibes", cursive;
    font-size: 92px;
    fill: var(--honey-gold);
  }
  .website {
    font-family: "Open Sans", sans-serif;
    font-weight: 700;
    font-size: 30px;
    fill: var(--text-white);
  }
  .net-weight {
    font-family: "Open Sans", sans-serif;
    font-weight: 600;
    font-size: 30px;
    fill: var(--honey-gold);
  }
</style>
</head>
<body>
<svg class="label-canvas" viewBox="0 0 1200 1101" xmlns="http://www.w3.org/2000/svg" aria-label="Pure Raw Honeycomb oval label">
  <defs>
    <path id="title-arc" d="M 220 550 A 380 215 0 0 1 980 550"/>
  </defs>

  <ellipse class="label-body" cx="600" cy="550" rx="490" ry="300"/>
  <ellipse class="label-rim" cx="600" cy="550" rx="466" ry="278"/>

  <text class="product-title" text-anchor="middle">
    <textPath href="#title-arc" startOffset="50%">Pure Raw Honeycomb</textPath>
  </text>

  <text class="brand-name" x="600" y="630" text-anchor="middle">Hive Lantern Gold</text>

  <text class="website" x="600" y="730" text-anchor="middle">www.hivelanterngold.ca</text>
  <text class="net-weight" x="600" y="780" text-anchor="middle">300 g</text>
</svg>
</body>
</html>
```